KR Stationary Design

Logo, Business Card, Letterhead & Email Signature Design

Target Market(s)

Legal

Colors

Designer to choose colors to be used in the design.

Requirements
Must have
• Gold and Blue are the colours to use. The KR must be inside the Gold Legal Pendulum

```html
<!DOCTYPE html>
<html lang="en">
<head>
<meta charset="utf-8">
<title>KR Stationery Set</title>
<link rel="stylesheet" href="https://fonts.googleapis.com/css2?family=Lato:wght@400;700&family=Merriweather:wght@700;900&display=swap">
<style>
:root{
  --navy:#2a2360;
  --gold:#f0bb6b;
  --ink:#6d6e71;
  --paper:#ffffff;
  --backdrop:#d4d5d7;
  --tint:#eef0f6;
}
*{box-sizing:border-box;margin:0;padding:0}
html,body{width:1200px;height:1200px;overflow:hidden;background:var(--backdrop)}
body{position:relative;font-family:"Lato",sans-serif;color:var(--ink)}
.sheet{position:absolute;background:var(--paper);overflow:hidden}
.brand{position:absolute;display:flex;align-items:center;gap:.45em;font-family:"Merriweather",serif;font-weight:900;color:var(--gold);white-space:nowrap;line-height:1}
.brand .dot{width:1.1em;height:1.1em;border-radius:50%;background:var(--navy);flex:none}
.brand.on-navy{color:var(--paper)}
.brand.on-navy .dot{background:var(--gold)}
.serif-sub{font-family:"Merriweather",serif;font-weight:700;color:var(--navy)}
.icon{width:1em;height:1em;fill:var(--navy);flex:none;margin-top:.1em}
.contact-row{display:flex;gap:.55em;align-items:flex-start}

/* Letterhead */
.letterhead{left:88px;top:252px;width:504px;height:713px}
.letterhead .brand{left:30px;top:74px;font-size:16px}
.letterhead .brand-sub{position:absolute;left:57px;top:91px;font-size:8px}
.letterhead .reg{position:absolute;left:29px;top:110px;font-size:8.2px}
.letterhead .contacts{position:absolute;left:378px;top:69px;font-size:6.6px;line-height:8.3px;display:flex;flex-direction:column;gap:1.2px}
.letterhead .contacts .addr{margin-top:3px}
.letter-body{position:absolute;left:32px;top:172px;width:442px;font-size:8.4px;line-height:11px}
.letter-body .date{margin-bottom:10px}
.letter-body .recipient{margin-bottom:29px}
.letter-body .salutation{color:#222;margin-bottom:17px}
.letter-body p{text-align:justify;margin-bottom:14px}
.closing{position:absolute;left:32px;top:516px}
.closing .name{font-family:"Merriweather",serif;font-weight:400;font-size:10.5px;color:#222;letter-spacing:.2px}
.closing .role{font-size:8.4px;margin-top:1px}
.signature-area{position:absolute;left:32px;top:546px;width:88px;height:38px;background:var(--tint);border-radius:3px}
.footer-band{position:absolute;left:0;bottom:0;width:100%;height:19px}
.footer-band .text{position:absolute;left:32px;top:4px;font-size:8.2px;color:var(--paper)}

/* Business card */
.card-front{left:576px;top:406px;width:214px;height:122px}
.card-front .brand{left:20px;top:28px;font-size:7px}
.card-front .brand-sub{position:absolute;left:28px;top:36px;font-size:3.6px}
.card-front .person{position:absolute;left:130px;top:25px;font-family:"Merriweather",serif;font-weight:900;color:var(--gold);font-size:7.4px}
.card-front .person-role{position:absolute;left:130px;top:35px;font-size:4.2px}
.card-front .contacts{position:absolute;left:20px;top:62px;font-size:4.4px;line-height:5.6px;display:flex;flex-direction:column;gap:1.2px}
.card-band{position:absolute;left:0;bottom:0;width:100%;height:8px}
.card-back{left:576px;top:558px;width:214px;height:122px;background:var(--navy)}
.card-back .brand{left:61px;top:54px;font-size:10.5px}
.card-back .brand-sub{position:absolute;left:82px;top:67px;font-size:5px;color:var(--paper)}

/* Email signature */
.email-sig{left:561px;top:742px;width:552px;height:127px}
.email-sig .person{position:absolute;left:41px;top:17px;font-family:"Merriweather",serif;font-weight:900;color:var(--gold);font-size:22px;line-height:1}
.email-sig .person-role{position:absolute;left:41px;top:43px;font-size:12.5px}
.email-sig .col{position:absolute;top:71px;font-size:7.8px;line-height:9.6px;display:flex;flex-direction:column;gap:4px}
.email-sig .col.left{left:41px}
.email-sig .col.right{left:109px}
.email-sig .brand{left:302px;top:35px;font-size:20px}
.email-sig .brand-sub{position:absolute;left:385px;top:57px;font-size:11px}
.socials{position:absolute;left:391px;top:84px;display:flex;gap:12px}
.socials span{width:12px;height:12px;border-radius:50%;background:var(--navy)}
.sig-band{position:absolute;left:0;bottom:0;width:100%;height:12px}
</style>
</head>
<body>
<svg width="0" height="0" style="position:absolute" aria-hidden="true">
  <symbol id="i-phone" viewBox="0 0 24 24"><path d="M6.6 10.8a15 15 0 0 0 6.6 6.6l2.2-2.2a1 1 0 0 1 1-.25 11.4 11.4 0 0 0 3.6.57 1 1 0 0 1 1 1V20a1 1 0 0 1-1 1A17 17 0 0 1 3 4a1 1 0 0 1 1-1h3.5a1 1 0 0 1 1 1c0 1.25.2 2.45.57 3.57a1 1 0 0 1-.25 1z"/></symbol>
  <symbol id="i-fax" viewBox="0 0 24 24"><path d="M6 2h10l2 2v5H6zM3 10h18a1 1 0 0 1 1 1v9a1 1 0 0 1-1 1H3a1 1 0 0 1-1-1v-9a1 1 0 0 1 1-1zm3 3v2h4v-2zm0 4v2h12v-2z"/></symbol>
  <symbol id="i-send" viewBox="0 0 24 24"><path d="M22 2 2 10l7 3 3 8z M9 13l13-11"/></symbol>
  <symbol id="i-pin" viewBox="0 0 24 24"><path d="M12 2a7 7 0 0 0-7 7c0 5 7 13 7 13s7-8 7-13a7 7 0 0 0-7-7zm0 10a3 3 0 1 1 0-6 3 3 0 0 1 0 6z"/></symbol>
  <symbol id="band" viewBox="0 0 100 10" preserveAspectRatio="none"><rect width="100" height="10" fill="#2a2360"/><polygon points="81,0 100,0 100,10 78.5,10" fill="#fff"/><polygon points="83,0 100,0 100,10 80.5,10" fill="#f0bb6b"/></symbol>
</svg>

<section class="sheet letterhead" aria-label="Letterhead">
  <div class="brand"><span class="dot"></span>Keswell</div>
  <div class="brand-sub serif-sub">Incorporated</div>
  <div class="reg">Reg: 2019/123456/07</div>
  <div class="contacts">
    <div class="contact-row"><svg class="icon"><use href="#i-phone"/></svg>011 555 0190</div>
    <div class="contact-row"><svg class="icon"><use href="#i-fax"/></svg>086 555 0148</div>
    <div class="contact-row"><svg class="icon"><use href="#i-send"/></svg>info@keswell-law.co.za</div>
    <div class="contact-row addr"><svg class="icon"><use href="#i-pin"/></svg><span>Block C Linden Office<br>Park 9 Oak road north<br>Sandton 2196</span></div>
  </div>
  <div class="letter-body">
    <div class="date">18.09.2019</div>
    <div class="recipient">Recipient name<br>42 Maple Ave.<br>Lakeview, PA 19000</div>
    <div class="salutation">Dear, Mr___________</div>
    <p>Lorem Ipsum is simply dummy text of the printing and typesetting industry. Lorem Ipsum has been the industry's standard dummy text ever since the1500s,when an unknown printer took a galley of type and scrambled it to make a type specimen book. It has survived not only five centuries, but also the leap into electronic typesetting, remaining essentially unchanged.</p>
    <p>Lorem Ipsum is simply dummy text of the printing and typesetting industry. Lorem Ipsum has been the industry's standard dummy text ever since the 1500s, when an unknown printer took a galley of type and scrambled it to make a type specimen book. It has survived not only five centuries, but also the leap into electronic typesetting, remaining essentially unchanged. It was popularised in the 1960s with the release of Letraset sheets containing Lorem Ipsum passages, and more recently with desktop publishing software including versions of Lorem Ipsum.</p>
    <p>Lorem Ipsum is simply dummy text of the printing and typesetting industry. Lorem Ipsum has been the industry's standard dummy text ever since the1500s.</p>
    <p>Lorem Ipsum is simply dummy text of the printing and typesetting industry. Lorem Ipsum has been the industry's standard dummy text ever since the1500s,when an unknown printer took a galley of type and scrambled it to make a type specimen book.</p>
  </div>
  <div class="closing">
    <div class="name">YOUR NAME</div>
    <div class="role">Designation</div>
  </div>
  <div class="signature-area" role="img" aria-label="Handwritten signature"></div>
  <div class="footer-band">
    <svg width="100%" height="100%"><use href="#band"/></svg>
    <div class="text">Director: Kagiso Thabo Rendell BA, LLB and HDip Tax Law</div>
  </div>
</section>

<section class="sheet card-front" aria-label="Business card front">
  <div class="brand"><span class="dot"></span>Keswell</div>
  <div class="brand-sub serif-sub">Incorporated</div>
  <div class="person">Kiran Rendell</div>
  <div class="person-role serif-sub">Director</div>
  <div class="contacts">
    <div class="contact-row"><svg class="icon"><use href="#i-phone"/></svg>011 555 0190</div>
    <div class="contact-row"><svg class="icon"><use href="#i-fax"/></svg>086 555 0148</div>
    <div class="contact-row"><svg class="icon"><use href="#i-send"/></svg>kiran@keswell-law.co.za</div>
    <div class="contact-row"><svg class="icon"><use href="#i-pin"/></svg><span>Block C Linden Office Park 9 Oak road<br>north Sandton 2196</span></div>
  </div>
  <svg class="card-band" viewBox="0 0 100 10" preserveAspectRatio="none"><use href="#band"/></svg>
</section>

<section class="sheet card-back" aria-label="Business card back">
  <div class="brand on-navy"><span class="dot"></span>Keswell</div>
  <div class="brand-sub serif-sub">Incorporated</div>
</section>

<section class="sheet email-sig" aria-label="Email signature">
  <div class="person">Kiran Rendell</div>
  <div class="person-role serif-sub">Director</div>
  <div class="col left">
    <div class="contact-row"><svg class="icon"><use href="#i-phone"/></svg>011 555 0190</div>
    <div class="contact-row"><svg class="icon"><use href="#i-fax"/></svg>086 555 0148</div>
  </div>
  <div class="col right">
    <div class="contact-row"><svg class="icon"><use href="#i-send"/></svg>kiran@keswell-law.co.za</div>
    <div class="contact-row"><svg class="icon"><use href="#i-pin"/></svg><span>Block C Linden Office Park 9 Oak road<br>north Sandton 2196</span></div>
  </div>
  <div class="brand"><span class="dot"></span>Keswell</div>
  <div class="brand-sub serif-sub">Incorporated</div>
  <div class="socials" aria-label="Social media links"><span></span><span></span><span></span><span></span><span></span></div>
  <svg class="sig-band" viewBox="0 0 100 10" preserveAspectRatio="none"><use href="#band"/></svg>
</section>
</body>
</html>
```